Business Card Design Project

Hello Designers, hope you are all aiming enjoy the weekend
I have the Business Logo (uploaded), you can alter the color which ever way you think would work,
Im looking for a simple yet striking feel, something which will stay memorable (I have uploaded 3 examples for you to flick through)
Information on the card, will just be the bare minimum,
Double Sided
Info being
i.e.
Name
Number
Website
ABN
Tobin Wexmoor
+468213579 (singapore)
+315792846 (Australia)
+729384615 (America)
www.lomevu-linkup.example
ABN 86420913
Enjoy,
Tobin
Industry/Entity Type
Business
Look and feel
Each slider illustrates characteristics of the customer's brand and the style your logo design should communicate.

```html
<!DOCTYPE html>
<html lang="en">
<head>
<meta charset="utf-8">
<title>Lomevu Linkup — Business Card</title>
<link rel="stylesheet" href="https://fonts.googleapis.com/css2?family=Arimo:wght@400;700&display=swap">
<style>
  :root {
    --page-bg: #ece9e4;
    --front-navy: #1b4469;
    --back-grey: #8c8c8c;
    --brand-red: #c8203f;
    --logo-grey: #c6c6c6;
    --ink: #111111;
    --white: #ffffff;
    --card-shadow: 0 10px 28px rgba(0, 0, 0, 0.22);
  }
  * { box-sizing: border-box; margin: 0; padding: 0; }
  html, body {
    width: 1200px;
    height: 800px;
    overflow: hidden;
    background: var(--page-bg);
    font-family: "Arimo", Arial, sans-serif;
  }
  .canvas {
    position: relative;
    width: 1200px;
    height: 800px;
    display: flex;
    align-items: center;
    justify-content: center;
    gap: 60px;
  }
  .card {
    position: relative;
    width: 520px;
    height: 306px;
    border-radius: 26px;
    box-shadow: var(--card-shadow);
    overflow: hidden;
  }
  /* Front side */
  .card--front {
    background: var(--front-navy);
  }
  .front-brand {
    position: absolute;
    left: 0;
    right: 0;
    top: 112px;
    display: flex;
    align-items: center;
    justify-content: center;
    gap: 16px;
  }
  .brand-square {
    width: 52px;
    height: 52px;
    background: var(--brand-red);
  }
  .front-brand .brand-name {
    font-size: 46px;
    font-weight: 400;
    color: var(--logo-grey);
    letter-spacing: 0.5px;
  }
  .front-website {
    position: absolute;
    left: 0;
    right: 0;
    bottom: 22px;
    text-align: center;
    font-size: 12.5px;
    color: var(--white);
    letter-spacing: 4px;
  }
  /* Back side */
  .card--back {
    background: var(--back-grey);
  }
  .back-brand {
    position: absolute;
    left: 40px;
    top: 44px;
    font-size: 30px;
    font-weight: 400;
    color: var(--brand-red);
    letter-spacing: 0.3px;
  }
  .contact {
    position: absolute;
    left: 300px;
    top: 150px;
    color: var(--ink);
    font-size: 13px;
    line-height: 1.3;
    font-style: normal;
  }
  .contact .contact-name {
    font-weight: 700;
    font-size: 13.5px;
    margin-bottom: 12px;
  }
  .contact p { margin: 0; }
</style>
</head>
<body>
  <main class="canvas">
    <section class="card card--front" aria-label="Business card front">
      <div class="front-brand">
        <span class="brand-square" aria-hidden="true"></span>
        <span class="brand-name">Lomevu Linkup</span>
      </div>
      <p class="front-website">www.lomevu-linkup.example</p>
    </section>

    <section class="card card--back" aria-label="Business card back">
      <p class="back-brand">Lomevu Linkup</p>
      <address class="contact">
        <p class="contact-name">Tobin Wexmoor</p>
        <p>+468213579 (singapore)</p>
        <p>+315792846 (Australia)</p>
        <p>+729384615 (America)</p>
        <p>www.lomevu-linkup.example</p>
        <p>ABN 86420913</p>
      </address>
    </section>
  </main>
</body>
</html>
```